Paper Lantern Theory - Podcast Cover

Paper Lantern Theory is a weekly podcast that dispels some of the myths about conventional economic thinking and provides a new way of thinking about issues that are faced by the global economy. It's insightful, thought-provoking and, most importantly, fun. We are refreshing the look and sound of the podcast. I have attached a copy of the old amateur design (which I did!)

Target Market(s)

Male oriented, smart folk with an interest in politics and economics

Font styles to use
Sans Serif

Requirements
Must have
• Clearly visible title, even when reduced in size. Must be 3000 pixels by 3000 pixels.
Nice to have
• This podcast challenges the status quo. It should reflect that. Photos and names of the hosts. Actually, because th ephotos are so different, we'd be open to the idea of a caricature if you can do that within the price.

```html
<!DOCTYPE html>
<html lang="en">
<head>
<meta charset="utf-8">
<title>The Paper Lantern Theory Podcast – Cover</title>
<link rel="stylesheet" href="https://fonts.googleapis.com/css2?family=Archivo+Black&family=Caveat:wght@600&display=swap">
<style>
  :root {
    --paper: #f5f5f5;
    --ink: #000000;
    --white: #ffffff;
    --red: #ed1c24;
    --green: #8dc63f;
    --bar-top: #b0b0b0;
    --grid: #c8c8c8;
    --host-left: #2e93a8;
    --host-right: #e8e6e0;
  }
  * { margin: 0; padding: 0; box-sizing: border-box; }
  html, body { width: 1200px; height: 1200px; overflow: hidden; background: var(--ink); }
  .cover { position: relative; width: 1200px; height: 1200px; background: var(--ink); font-family: "Archivo Black", "Arial Black", sans-serif; }
  .stage { position: absolute; left: 0; top: 0; width: 1200px; height: 529px; background: var(--paper); overflow: hidden; }
  .chart { position: absolute; inset: 0; }
  .host-photo { position: absolute; }
  .host-name { position: absolute; line-height: 1; text-transform: uppercase; }
  .host-name span { display: block; }
  .host-name .first { color: var(--ink); }
  .host-name .last { color: var(--red); }
  .host-name--left { left: 74px; top: 158px; font-size: 36px; text-align: right; width: 170px; }
  .host-name--right { right: 78px; top: 222px; font-size: 36px; text-align: right; }
  .host-title { position: absolute; right: 128px; top: 176px; font-family: "Caveat", cursive; font-size: 30px; color: var(--red); }
  .title-block { position: absolute; left: 0; top: 529px; width: 1200px; height: 671px; color: var(--white); text-align: center; }
  .rule-line { position: absolute; display: flex; align-items: center; left: 82px; right: 90px; gap: 34px; }
  .rule-line::before, .rule-line::after { content: ""; flex: 1; height: 3px; background: var(--white); }
  .rule-line--the { top: 105px; font-size: 84px; line-height: 1; }
  .rule-line--podcast { top: 493px; font-size: 78px; line-height: 1; }
  .show-name { position: absolute; left: 0; width: 1200px; color: var(--red); line-height: 1; text-transform: uppercase; }
  .show-name--top { top: 220px; font-size: 111px; letter-spacing: -2px; }
  .show-name--bottom { top: 345px; font-size: 150px; letter-spacing: 14px; }
</style>
</head>
<body>
<main class="cover">
  <section class="stage">
    <svg class="chart" width="1200" height="529" viewBox="0 0 1200 529">
      <defs>
        <linearGradient id="barFade" x1="0" y1="0" x2="0" y2="1">
          <stop offset="0" stop-color="var(--bar-top)" stop-color-opacity="1" style="stop-color:#b0b0b0"/>
          <stop offset="1" style="stop-color:#f5f5f5"/>
        </linearGradient>
      </defs>
      <g class="bars" fill="url(#barFade)">
        <rect x="84" y="245" width="94" height="200"/>
        <rect x="200" y="193" width="94" height="260"/>
        <rect x="406" y="154" width="94" height="300"/>
        <rect x="523" y="219" width="95" height="240"/>
        <rect x="651" y="116" width="94" height="320"/>
        <rect x="772" y="178" width="94" height="280"/>
        <rect x="940" y="204" width="43" height="260"/>
        <rect x="1005" y="176" width="94" height="280"/>
      </g>
      <g class="grid" stroke="#c8c8c8" stroke-width="1">
        <line x1="58" y1="298" x2="1120" y2="298"/>
        <line x1="58" y1="376" x2="1120" y2="376"/>
        <line x1="58" y1="455" x2="1120" y2="455"/>
      </g>
      <g class="trend" stroke="#8dc63f" stroke-width="3" fill="none" stroke-linejoin="miter">
        <polyline points="463,323 544,255 625,346 752,197"/>
      </g>
      <polygon class="trend-head" fill="#8dc63f" points="764,183 734,198 752,214"/>
    </svg>

    <svg class="host-photo" style="left:74px;top:78px" width="534" height="451" viewBox="0 0 534 451" role="img" aria-label="Photo of host Mark Tallow, smiling, in a teal polo shirt">
      <path d="M0,451 L14,330 Q30,245 150,215 L190,200 L200,150 Q180,80 215,30 Q270,-5 330,20 Q370,60 350,150 L340,200 L420,220 Q515,250 534,380 L534,451 Z" fill="#2e93a8"/>
    </svg>

    <svg class="host-photo" style="left:675px;top:70px" width="385" height="459" viewBox="0 0 385 459" role="img" aria-label="Photo of host Owen Hartley in a light grey T-shirt">
      <path d="M0,420 L10,300 Q20,235 95,220 L150,200 L150,150 Q135,60 170,20 Q220,-10 270,20 Q295,60 285,150 L275,200 L320,225 Q370,245 380,330 L385,459 L0,459 Z" fill="#e8e6e0"/>
    </svg>

    <h2 class="host-name host-name--left"><span class="first">Mark</span><span class="last">Tallow</span></h2>
    <p class="host-title">Prof</p>
    <h2 class="host-name host-name--right"><span class="first">Owen</span><span class="last">Hartley</span></h2>
  </section>

  <header class="title-block">
    <div class="rule-line rule-line--the">THE</div>
    <h1>
      <span class="show-name show-name--top">Paper Lantern</span>
      <span class="show-name show-name--bottom">Theory</span>
    </h1>
    <div class="rule-line rule-line--podcast">PODCAST</div>
  </header>
</main>
</body>
</html>
```